Sports Graphic Templates for Action Photos

I am looking for a graphic design template for sports action photos. This needs to be simple enough that someone without expertise in Photoshop (use this program) can upload an image into a layer or what not and export the file for use.

The file needs to be 1280x720 and MUST incorporate the attached QUILLS graphic in some form or fashion. How is up to you.

Orbitron and DinPro are the two fonts I want to have used in the design. It can be one or it can be both.

Ideally - this template can be used for multiple graphics using similar action shots. Athlete of the Week or Athlete of the Year are two examples.

One other note - the QUILLS graphic needs to be incorporated somehow and it would be good to be able to interchange the coloring. The file uploaded is blue but we'd like to be able to match the colors to other photos or pull coloring from other parts of the image.

The image or action shot must not be cut out or altered other than to have certain styles applied. As mentioned above this would need to be updated by someone with limited Photoshop knowledge.

Examples:

http://www.hoopvarta.com/falconers/releases/player-of-the-week-doran-160404

https://tessmorathletics.com/news/2017/10/9/womens-soccer-lisa-varnet-adds-another-coral-ridge-player-of-the-week-award.aspx?path=wsoc

http://www.hoopvarta.com/tavin-week

https://k7pwm2zrfaqo58.imgvaultcdn.net/900x407_/media/14124/2560x1300-potywinner-belcastro.jpg

https://morvenhawks.com/images/2017/5/15/SB_Lakeshore_9_Awards_Social_Media_Graphic_Greta_Solvik_v1.jpg

https://thumbs-qx4.pictorelay.net/images?q=tbn:Vx82hTqLm04-77pR3KWdsZeBn91CfuAh56JoNwYtLqEaQ3XKrb9m

Target Market(s)

Action Shots Highlighting Achievement

Font styles to use
Other font styles liked:
• Orbitron and DinPro - one or both of those

Colors

Designer to choose colors to be used in the design.

Requirements
Must have
• Photoshop design. Use of the QUILLS graphis supplied - fonts (one or both) - 1280x720 sizing.
• Easy to use - someone with limited knowledge can easily update.
Nice to have
• Something that stands out from the rest. Examples were shown - none of those incorporate an action shot without the cutting out of the action or person in the image.
Should not have
• Any non-free textures or other items that need to be purchased.

```html
<!DOCTYPE html>
<html lang="en">
<head>
<meta charset="utf-8">
<title>Athlete of the Year – Template Board</title>
<link rel="stylesheet" href="https://fonts.googleapis.com/css2?family=Orbitron:wght@700;900&family=Barlow+Condensed:wght@700&family=Roboto:wght@400&display=swap">
<style>
  :root{
    --board:#ffffff;
    --metal-light:#ffffff;
    --metal-mid:#9a9ea3;
    --metal-dark:#d9dcdf;
    --gold-edge:#b88a3e;
    --name-ink:#f3ead8;
    --panel-bg:#2c2c2c;
    --panel-row:#323232;
    --panel-line:#3d3d3d;
    --panel-text:#d6d6d6;
    --panel-dim:#8b8b8b;
  }
  *{box-sizing:border-box;margin:0;padding:0}
  html,body{width:1200px;height:1200px;overflow:hidden;background:var(--board)}
  .board{position:relative;width:1200px;height:1200px}

  .poster{position:absolute;display:block;box-shadow:0 8px 28px rgba(0,0,0,.35)}
  .poster--hero{left:63px;top:50px;width:1073px;height:604px}
  .poster--red{left:63px;top:692px;width:465px;height:260px}
  .poster--blue{left:403px;top:890px;width:463px;height:261px}

  .theme-teal{--tone-deep:#071a1e;--tone-mid:#1b4a50;--tone-glow:#3f6f6c;--accent:#1f8088}
  .theme-red{--tone-deep:#1c0506;--tone-mid:#5a1416;--tone-glow:#8a3a33;--accent:#a2262a}
  .theme-blue{--tone-deep:#061421;--tone-mid:#173b58;--tone-glow:#5b6670;--accent:#1f6591}

  .stop-deep{stop-color:var(--tone-deep)}
  .stop-mid{stop-color:var(--tone-mid)}
  .stop-glow{stop-color:var(--tone-glow)}
  .stripes{fill:var(--accent)}

  .title-name{font-family:"Barlow Condensed","DIN Pro",sans-serif;font-weight:700;font-size:60px;fill:var(--name-ink);stroke:var(--gold-edge);stroke-width:1.5;paint-order:stroke}
  .title-main{font-family:"Orbitron",sans-serif;font-weight:900;font-size:150px;fill:url(#metal);stroke:var(--gold-edge);stroke-width:3;paint-order:stroke}
  .title-sub{font-family:"Orbitron",sans-serif;font-weight:900;font-size:76px;fill:url(#metal);stroke:var(--gold-edge);stroke-width:2.5;paint-order:stroke}
  .title-shadow{filter:drop-shadow(0 4px 6px rgba(0,0,0,.7))}

  /* layers panel */
  .layers{position:absolute;left:889px;top:692px;width:247px;height:459px;background:var(--panel-bg);
    font-family:"Roboto",sans-serif;font-size:7px;color:var(--panel-text);box-shadow:0 8px 28px rgba(0,0,0,.35);overflow:hidden}
  .layers__tab{height:22px;padding:9px 6px 0;border-bottom:1px solid var(--panel-line);font-size:7px}
  .layers__tools{height:40px;border-bottom:1px solid var(--panel-line);padding:6px;display:flex;flex-direction:column;gap:6px;color:var(--panel-dim)}
  .layers__tools span{display:block}
  .layers__list{list-style:none}
  .layer{position:relative;height:25.6px;display:flex;align-items:center;border-bottom:1px solid var(--panel-line);padding-left:6px}
  .layer--group{height:20px}
  .layer__eye{width:7px;height:4px;border:1px solid var(--panel-text);border-radius:50%;margin-right:10px;flex:none}
  .layer__eye--off{border-color:transparent}
  .layer__indent{width:22px;flex:none}
  .layer__folder{width:8px;height:6px;border:1px solid var(--panel-text);margin-right:6px;flex:none}
  .layer__type{font-family:"Orbitron",sans-serif;font-size:9px;width:24px;text-align:center;margin-right:6px;flex:none}
  .layer__thumb{width:34px;height:18px;margin-right:4px;flex:none;border:1px solid #555}
  .layer__mask{width:34px;height:18px;margin-right:6px;flex:none;background:radial-gradient(ellipse at center,#000 40%,#fff 75%)}
  .layer__mask--white{background:#fff}
  .layer__name{flex:1;white-space:nowrap;overflow:hidden}
  .layer__fx{position:absolute;right:14px;color:var(--panel-dim);font-style:italic}
  .layer__lock{position:absolute;right:12px;width:6px;height:6px;border:1px solid var(--panel-dim)}
  .thumb-teal{background:#1d4f55}
  .thumb-lines{background:repeating-linear-gradient(135deg,#2a9aa2 0 3px,#e6e6e6 3px 6px)}
  .thumb-black{background:#050505}
  .thumb-check{background:repeating-conic-gradient(#bbb 0 25%,#eee 0 50%) 0 0/6px 6px}
  .thumb-blue{background:linear-gradient(135deg,#0d3a7a,#2a7ad0)}
  .thumb-photo{background:linear-gradient(135deg,#3a4a5a,#7a6a5a)}
  .thumb-white{background:#fff}
  .italic{font-style:italic}
</style>
</head>
<body>
<main class="board">

  <svg width="0" height="0" style="position:absolute" aria-hidden="true">
    <defs>
      <linearGradient id="metal" x1="0" y1="0" x2="0" y2="1">
        <stop offset="0" stop-color="#ffffff"/>
        <stop offset=".45" stop-color="#c9ccd0"/>
        <stop offset=".55" stop-color="#8f9499"/>
        <stop offset="1" stop-color="#eceef0"/>
      </linearGradient>
    </defs>
  </svg>

  <!-- hero poster -->
  <svg class="poster poster--hero theme-teal" viewBox="0 0 1280 720" preserveAspectRatio="none">
    <defs>
      <radialGradient id="photo-teal" cx=".55" cy=".4" r=".7">
        <stop class="stop-glow" offset="0"/><stop class="stop-mid" offset=".45"/><stop class="stop-deep" offset="1"/>
      </radialGradient>
    </defs>
    <rect width="1280" height="720" fill="url(#photo-teal)" role="img" aria-label="Action photo of a wheelchair racer in a green team shirt and white helmet"/>
    <g class="stripes" opacity=".7">
      <g transform="translate(-40 -120) rotate(50)">
        <rect x="0" y="0" width="520" height="22"/><rect x="40" y="40" width="420" height="10"/>
        <rect x="80" y="70" width="360" height="28"/><rect x="20" y="115" width="300" height="8"/>
        <rect x="120" y="140" width="260" height="18"/><rect x="60" y="175" width="200" height="6"/>
        <rect x="0" y="200" width="160" height="24"/>
      </g>
      <g transform="translate(1120 430) rotate(50)">
        <rect x="0" y="0" width="520" height="24"/><rect x="-40" y="45" width="460" height="10"/>
        <rect x="-20" y="75" width="420" height="30"/><rect x="-60" y="125" width="380" height="8"/>
        <rect x="0" y="150" width="300" height="20"/><rect x="-30" y="190" width="240" height="12"/>
      </g>
    </g>
    <g class="title-shadow" text-anchor="middle">
      <text class="title-name" x="639" y="402" textLength="284" lengthAdjust="spacingAndGlyphs">JOHN SMITH</text>
      <text class="title-main" x="664" y="550" textLength="811" lengthAdjust="spacingAndGlyphs">ATHLETE</text>
      <text class="title-sub" x="640" y="625" textLength="578" lengthAdjust="spacingAndGlyphs">OF THE YEAR</text>
    </g>
  </svg>

  <!-- red variant -->
  <svg class="poster poster--red theme-red" viewBox="0 0 1280 720" preserveAspectRatio="none">
    <defs>
      <radialGradient id="photo-red" cx=".6" cy=".35" r=".7">
        <stop class="stop-glow" offset="0"/><stop class="stop-mid" offset=".45"/><stop class="stop-deep" offset="1"/>
      </radialGradient>
    </defs>
    <rect width="1280" height="720" fill="url(#photo-red)" role="img" aria-label="Action photo of a wheelchair racer tinted red"/>
    <g class="stripes" opacity=".7">
      <g transform="translate(-40 -120) rotate(50)">
        <rect x="0" y="0" width="520" height="22"/><rect x="40" y="40" width="420" height="10"/>
        <rect x="80" y="70" width="360" height="28"/><rect x="20" y="115" width="300" height="8"/>
        <rect x="120" y="140" width="260" height="18"/><rect x="0" y="200" width="160" height="24"/>
      </g>
    </g>
    <g class="title-shadow" text-anchor="middle">
      <text class="title-name" x="640" y="412" textLength="284" lengthAdjust="spacingAndGlyphs">JOHN SMITH</text>
      <text class="title-main" x="640" y="560" textLength="811" lengthAdjust="spacingAndGlyphs">ATHLETE</text>
      <text class="title-sub" x="640" y="645" textLength="578" lengthAdjust="spacingAndGlyphs">OF THE YEAR</text>
    </g>
  </svg>

  <!-- blue variant -->
  <svg class="poster poster--blue theme-blue" viewBox="0 0 1280 720" preserveAspectRatio="none">
    <defs>
      <radialGradient id="photo-blue" cx=".55" cy=".3" r=".7">
        <stop class="stop-glow" offset="0"/><stop class="stop-mid" offset=".45"/><stop class="stop-deep" offset="1"/>
      </radialGradient>
    </defs>
    <rect width="1280" height="720" fill="url(#photo-blue)" role="img" aria-label="Action photo of a weightlifter straining under a barbell, tinted blue"/>
    <g class="stripes" opacity=".7">
      <g transform="translate(-40 -120) rotate(50)">
        <rect x="0" y="0" width="520" height="22"/><rect x="40" y="40" width="420" height="10"/>
        <rect x="80" y="70" width="360" height="28"/><rect x="20" y="115" width="300" height="8"/>
        <rect x="120" y="140" width="260" height="18"/><rect x="0" y="200" width="160" height="24"/>
      </g>
      <g transform="translate(1120 430) rotate(50)">
        <rect x="0" y="0" width="520" height="24"/><rect x="-40" y="45" width="460" height="10"/>
        <rect x="-20" y="75" width="420" height="30"/><rect x="0" y="150" width="300" height="20"/>
      </g>
    </g>
    <g class="title-shadow" text-anchor="middle">
      <text class="title-name" x="640" y="412" textLength="284" lengthAdjust="spacingAndGlyphs">JOHN SMITH</text>
      <text class="title-main" x="640" y="560" textLength="811" lengthAdjust="spacingAndGlyphs">ATHLETE</text>
      <text class="title-sub" x="640" y="645" textLength="578" lengthAdjust="spacingAndGlyphs">OF THE YEAR</text>
    </g>
  </svg>

  <!-- layers panel -->
  <section class="layers" aria-label="Template layer structure">
    <div class="layers__tab">Layers</div>
    <div class="layers__tools">
      <span>Kind &nbsp; ▢ ◐ T ⌗</span>
      <span>Normal &nbsp;&nbsp;&nbsp;&nbsp;&nbsp; Opacity: 100% &nbsp;&nbsp; Fill: 100%</span>
    </div>
    <ul class="layers__list">
      <li class="layer layer--group"><span class="layer__eye"></span><span class="layer__folder"></span><span class="layer__name">Text</span></li>
      <li class="layer"><span class="layer__eye"></span><span class="layer__indent"></span><span class="layer__type">T</span><span class="layer__name">John Smith</span><span class="layer__fx">fx</span></li>
      <li class="layer"><span class="layer__eye"></span><span class="layer__indent"></span><span class="layer__type">T</span><span class="layer__name">Athlete</span><span class="layer__fx">fx</span></li>
      <li class="layer"><span class="layer__eye"></span><span class="layer__indent"></span><span class="layer__type">T</span><span class="layer__name">of The Year</span><span class="layer__fx">fx</span></li>
      <li class="layer layer--group"><span class="layer__eye"></span><span class="layer__folder"></span><span class="layer__name">Effect</span></li>
      <li class="layer"><span class="layer__eye"></span><span class="layer__indent"></span><span class="layer__thumb thumb-teal"></span><span class="layer__mask layer__mask--white"></span><span class="layer__name">Color Fill 1</span></li>
      <li class="layer"><span class="layer__eye"></span><span class="layer__indent"></span><span class="layer__thumb thumb-lines"></span><span class="layer__name">Geometric Line</span></li>
      <li class="layer"><span class="layer__eye"></span><span class="layer__indent"></span><span class="layer__thumb thumb-black"></span><span class="layer__name">Star-Effect</span></li>
      <li class="layer"><span class="layer__eye"></span><span class="layer__indent"></span><span class="layer__thumb thumb-check"></span><span class="layer__name">Vignette</span></li>
      <li class="layer"><span class="layer__eye"></span><span class="layer__thumb thumb-blue"></span><span class="layer__mask"></span><span class="layer__name">mood image blue small</span></li>
      <li class="layer"><span class="layer__eye"></span><span class="layer__indent"></span><span class="layer__mask"></span><span class="layer__name">Gradient Map 1</span></li>
      <li class="layer"><span class="layer__eye"></span><span class="layer__thumb thumb-check"></span><span class="layer__name">Vignette</span></li>
      <li class="layer layer--group"><span class="layer__eye"></span><span class="layer__folder"></span><span class="layer__name">Your Image Placed Here</span></li>
      <li class="layer"><span class="layer__eye"></span><span class="layer__indent"></span><span class="layer__thumb thumb-photo"></span><span class="layer__name">Your Image</span></li>
      <li class="layer"><span class="layer__eye layer__eye--off"></span><span class="layer__indent"></span><span class="layer__thumb thumb-photo"></span><span class="layer__name">weights-664766_960_720</span></li>
      <li class="layer"><span class="layer__eye"></span><span class="layer__thumb thumb-white"></span><span class="layer__name italic">Background</span><span class="layer__lock"></span></li>
    </ul>
  </section>

</main>
</body>
</html>
```